"The Craft of Patron Care," fourth edition cover design

Later this year, my publisher, Harold Penmarsh & Daughters, will issue a fourth, substantially revised edition of "The Craft of Patron Care," following the 2016 publication of the third edition and the second and first versions that were issued earlier.

To distinguish this new edition from previous ones, I need a cover design that visually connects and is consistent with what has preceded it, while signaling this is a new and different, worthy of prospective readers/buyers’ attention.

Attached are three different verbal approaches to the new cover; these are NOT MEANT to serve as actual designs, but rather will give you a sense of how language is to be deployed:

The first emphasizes “ART” as the key visual word in the book title;
The second emphasizes “CLIENT SERVICE” as the key visual words in the book title; and,
The third emphasizes just the word "CLIENT" in the book title.

A top-of-the-page is a pre-head that applies to all three versions:
“6 TIMELESS PRINCIPLES FOR ADVERTISING & MARKETING PRO’s
IN AN AI WORLD"

There's a mid-page sub-head for all three versions:
“THE CLASSIC GUIDE,” followed by
“FOURTH EDITION BY GERALD ASHCOMBE

And there's a one-line, bottom-of-the-page designation:
“Foreword by Mae Dunford, Global Executive Creative Director, Starbolt"

The pallette for the previously published third edition was black with red as an accent color on a field of white; I've attached a sample for reference, so you can see how it was executed. For this new fourth edition, I'd like to change the accent color from red to either Wedgewood blue, or British racing green, or an alternative that is assertive and color saturated -- think of primary colors -- that contrast sufficiently with the base of black. As an alternative, you can consider a cover that used either Wedgewood blue, British racing green, or another possibility as a full-bleed field, with copy content either revered out or surprinted.

Lastly, while the new cover largely is meant to be typographically driven, if you can come up with a visual metaphor that illustrates and builds on the book's title, that would be very helpful. By way of reference, the third edition's book cover attempted to do this by introducing a visual element at the end of the book's title that's meant to represent an artist's paint splatter (although I admit it didn't work as well as it should).

Target Market(s)

Prospective purchasers of the book who might discover copies at a bookstore, but more likely will encounter it through online distributors such as Riverdex, Hartwell & Pike, and Tindall’s.

Industry/Entity Type

Advertising and marketing

Font styles to use
Serif
Sans Serif
Other font styles liked:
• A mix of serif and san-serif typefaces is okay. for the examples I shared, I relieid on "Arial Rounded Bold" but you need not be weeded to this. If you opt to mix in a serif font, I am partial to Cambria as a typeface.

Requirements
Must have
• To achieve the goal of being “connected with but distinct” from previous editions, the new cover should be:  Largely typographic, but displaying a color palette different from the previous editions’ black-plus-red-accent on a canvas of white.  Any new accent color selected for use should be vibrant, strong, and highly saturated; think “British racing green,” “Wedgewood blue,” or their equivalents.  In addition to a powerful, “billboard” approach to type and color, consider other visual metaphors that are likely to engage the readers. The winning cover design will stand out from other books, while connecting with the previously published third edition.
Nice to have
• If you can find way to illustrate the book's title through a visual metaphor, that would be ideal.a
Should not have
• Anything that is frivolous or non-sensical

```html
<!DOCTYPE html>
<html lang="en">
<head>
<meta charset="utf-8">
<title>The Craft of Patron Care — Fourth Edition Cover</title>
<link rel="stylesheet" href="https://fonts.googleapis.com/css2?family=Dela+Gothic+One&family=Montserrat:wght@400;500;600;700;800;900&display=swap">
<style>
  :root {
    --racing-green: #0c4129;
    --ink: #1a1a1a;
    --ink-soft: #2b2b2b;
    --paper: #ffffff;
    --backdrop: #ededf2;
  }
  * { margin: 0; padding: 0; box-sizing: border-box; }
  html, body {
    width: 1200px; height: 1200px; overflow: hidden;
    background: var(--backdrop);
  }
  .cover {
    position: absolute; left: 200px; top: 0;
    width: 800px; height: 1200px;
    background: var(--paper);
    font-family: "Montserrat", sans-serif;
    color: var(--ink);
  }
  .prehead-bar {
    position: absolute; left: 92px; top: 84px;
    width: 194px; height: 64px;
    background: var(--racing-green);
    border-top-left-radius: 64px;
  }
  .prehead {
    position: absolute; left: 298px; top: 80px;
    font-size: 20px; line-height: 24.5px; font-weight: 400;
    color: var(--ink); letter-spacing: 0.2px;
  }
  .prehead strong { font-weight: 700; color: var(--racing-green); }
  .title { font-weight: normal; }
  .title-the {
    position: absolute; left: 134px; top: 306px;
    font-size: 84px; font-weight: 600; letter-spacing: 1px;
    line-height: 1; color: var(--ink);
  }
  .title-craft { position: absolute; left: 137px; top: 400px; width: 525px; height: 215px; }
  .title-of {
    position: absolute; left: 137px; top: 616px;
    font-size: 76px; font-weight: 700; line-height: 1;
    color: var(--ink);
  }
  .title-patron { position: absolute; left: 137px; top: 702px; width: 525px; height: 100px; }
  .title-care {
    position: absolute; right: 138px; top: 812px;
    font-size: 76px; font-weight: 500; line-height: 1;
    letter-spacing: 10px; margin-right: -10px;
    color: var(--ink-soft);
  }
  .edition {
    position: absolute; right: 475px; top: 1016px;
    text-align: right; line-height: 1;
  }
  .edition .guide { font-size: 13px; font-weight: 600; letter-spacing: 3.4px; margin-right: -3.4px; color: var(--ink); }
  .edition .number { font-size: 23px; font-weight: 800; letter-spacing: 2.4px; margin-right: -2.4px; color: var(--racing-green); margin-top: 5px; }
  .edition .author { font-size: 14px; font-weight: 800; letter-spacing: 3.6px; margin-right: -3.6px; color: var(--racing-green); margin-top: 5px; }
  .edition .author span { font-weight: 600; color: var(--ink); }
  .edition-bar {
    position: absolute; left: 333px; top: 1014px;
    width: 373px; height: 56px;
    background: var(--racing-green);
    border-top-right-radius: 56px;
  }
  .foreword {
    position: absolute; right: 92px; top: 1086px;
    text-align: right; font-size: 13px; line-height: 18.5px;
    font-weight: 500; color: var(--ink-soft);
  }
</style>
</head>
<body>
  <main class="cover">
    <div class="prehead-bar"></div>
    <p class="prehead"><strong>6 TIMELESS PRINCIPLES</strong><br>FOR ADVERTISING &amp; MARKETING PRO’s<br>IN AN AI WORLD</p>

    <h1 class="title">
      <span class="title-the">the</span>
      <svg class="title-craft" viewBox="0 0 525 215" aria-label="craft">
        <text x="0" y="180" textLength="525" lengthAdjust="spacingAndGlyphs"
              font-family="Montserrat, sans-serif" font-weight="900" font-size="238"
              fill="var(--racing-green)">craft</text>
      </svg>
      <span class="title-of">of</span>
      <svg class="title-patron" viewBox="0 0 525 100" aria-label="PATRON">
        <text x="0" y="98" textLength="525" lengthAdjust="spacingAndGlyphs"
              font-family="'Dela Gothic One', sans-serif" font-size="118"
              fill="var(--racing-green)">PATRON</text>
      </svg>
      <span class="title-care">CARE</span>
    </h1>

    <div class="edition">
      <p class="guide">THE CLASSIC GUIDE</p>
      <p class="number">FOURTH EDITION</p>
      <p class="author"><span>BY</span> GERALD ASHCOMBE</p>
    </div>
    <div class="edition-bar"></div>

    <p class="foreword">Foreword by Mae Dunford, Global Executive<br>Creative Director, Starbolt</p>
  </main>
</body>
</html>
```